Medical equipment business looking for professional, unique business card

We need a business card design for a durable medical equipment company. We are small but would like our cards to express that we are much bigger. We focus on braces (back, knee, wrist, etc) but also do crutches, rollators, wheelchairs- basically medical equipment that gets you going and back in Action. Our colors are blue and green and our logo has an arrow and use of a "spine". We'd like to express professionalism while being unique.

Industry/Entity Type

Medical Equipment

Contact Information for Business Card

Professional feel but unique. Memorable.

Font styles to use
Serif
Sans Serif
Other font styles liked:
• verdana

Requirements
Must have
• card holders cell#, business phone#, fax#, email, website address, business address, logo
Nice to have
• use of medical/healthcare related descriptive words, items, look
Should not have
• the wrong colors or cartoon characters.

```html
<!DOCTYPE html>
<html lang="en">
<head>
<meta charset="utf-8">
<title>Stride DME – Business Card</title>
<link rel="stylesheet" href="https://fonts.googleapis.com/css2?family=Quicksand:wght@400;500;600;700&display=swap">
<style>
  :root {
    --navy: #0b4468;
    --navy-deep: #083a5a;
    --green: #8dc63f;
    --white: #ffffff;
    --logo-blue: #14507a;
    --tag-blue: #2a8fd0;
    --backdrop: #e9ecef;
  }
  * { margin: 0; padding: 0; box-sizing: border-box; }
  html, body {
    width: 1200px; height: 902px; overflow: hidden;
    background: var(--backdrop);
    font-family: "Quicksand", "Verdana", sans-serif;
  }
  .card {
    position: absolute; left: 75px; top: 151px;
    width: 1050px; height: 600px;
    background: var(--navy);
    color: var(--white);
    box-shadow: 0 10px 30px rgba(0,0,0,.18);
    overflow: hidden;
  }
  .brand-band {
    position: absolute; right: 0; top: 0;
    width: 160px; height: 100%;
    background: var(--white);
  }
  .brand {
    position: absolute; left: 50%; top: 50%;
    transform: translate(-50%, -50%) rotate(90deg);
    width: 520px; text-align: center;
    display: flex; flex-direction: column; align-items: center;
  }
  .brand-name {
    display: flex; align-items: center; gap: 14px;
    font-size: 64px; font-weight: 700; color: var(--logo-blue);
    line-height: 1; white-space: nowrap;
  }
  .brand-dot {
    width: 26px; height: 26px; border-radius: 50%;
    background: var(--green);
  }
  .brand-tagline {
    margin-top: 8px;
    font-size: 20px; font-weight: 600; color: var(--tag-blue);
    letter-spacing: .5px; white-space: nowrap;
  }
  .holder { position: absolute; left: 62px; top: 90px; }
  .holder-name { font-size: 40px; font-weight: 500; letter-spacing: .5px; white-space: nowrap; }
  .holder-rule {
    position: absolute; left: 190px; top: 62px;
    width: 170px; height: 2px; background: var(--green);
  }
  .holder-title { font-size: 28px; font-weight: 500; margin: 8px 0 0 22px; }
  .contact-list { position: absolute; list-style: none; }
  .contact-list.personal { left: 80px; top: 265px; }
  .contact-list.office { right: 200px; top: 112px; text-align: right; }
  .contact-list li {
    display: flex; align-items: center; gap: 14px;
    font-size: 25px; height: 50px; white-space: nowrap;
  }
  .contact-list.office li { justify-content: flex-end; }
  .contact-list.office li.address { height: 70px; line-height: 1.2; }
  .divider { width: 2px; height: 30px; background: var(--green); flex: none; }
  .icon { width: 30px; height: 30px; flex: none; }
  .products-rule {
    position: absolute; left: 300px; top: 440px;
    width: 560px; height: 2px; background: var(--green);
  }
  .product-list {
    position: absolute; left: 300px; top: 480px; width: 570px;
    list-style: none; display: flex; justify-content: space-between;
  }
  .product-list li {
    display: flex; align-items: center;
    font-size: 29px; font-weight: 500; white-space: nowrap;
  }
  .product-list li::before {
    content: ""; flex: none; width: 9px; height: 9px;
    border-radius: 50%; background: var(--green);
    margin-right: 9px;
  }
</style>
</head>
<body>
  <article class="card">
    <section class="holder">
      <h1 class="holder-name">John Doe Senior</h1>
      <span class="holder-rule"></span>
      <p class="holder-title">Manager</p>
    </section>

    <ul class="contact-list personal">
      <li>
        <svg class="icon" viewBox="0 0 30 30" fill="none" stroke="#fff" stroke-width="2"><rect x="8" y="3" width="14" height="24" rx="2"/><line x1="13" y1="23" x2="17" y2="23"/></svg>
        <span class="divider"></span><span>123 . 456 . 789</span>
      </li>
      <li>
        <svg class="icon" viewBox="0 0 30 30"><rect x="3" y="7" width="24" height="16" fill="#fff"/><path d="M3 7 L15 17 L27 7" fill="none" stroke="#0b4468" stroke-width="2"/></svg>
        <span class="divider"></span><span>johnds@stridedme.com</span>
      </li>
      <li>
        <svg class="icon" viewBox="0 0 30 30" fill="none" stroke="#fff" stroke-width="2.2"><rect x="5" y="14" width="11" height="7" rx="3.5" transform="rotate(-45 10.5 17.5)"/><rect x="14" y="9" width="11" height="7" rx="3.5" transform="rotate(-45 19.5 12.5)"/></svg>
        <span class="divider"></span><span>www.stridedme.com</span>
      </li>
    </ul>

    <ul class="contact-list office">
      <li>
        <span>123 . 456 . 789</span><span class="divider"></span>
        <svg class="icon" viewBox="0 0 30 30"><path d="M8 4 L12 4 L13 10 L10 12 Q12 18 18 20 L20 17 L26 18 L26 22 Q25 26 21 26 Q6 24 4 9 Q4 5 8 4Z" fill="#fff"/></svg>
      </li>
      <li>
        <span>123 . 456 . 789</span><span class="divider"></span>
        <svg class="icon" viewBox="0 0 30 30" fill="#fff"><rect x="9" y="4" width="12" height="7"/><rect x="4" y="11" width="22" height="10" rx="2"/><rect x="9" y="18" width="12" height="8" stroke="#0b4468" stroke-width="1.5"/></svg>
      </li>
      <li class="address">
        <span>42 Riverside Walk<br>Kingston, London</span><span class="divider"></span>
        <svg class="icon" viewBox="0 0 30 30" fill="#fff"><path d="M15 4 L27 15 L23 15 L23 26 L17 26 L17 19 L13 19 L13 26 L7 26 L7 15 L3 15Z"/></svg>
      </li>
    </ul>

    <span class="products-rule"></span>
    <ul class="product-list">
      <li>braces</li>
      <li>crutches</li>
      <li>rollators</li>
      <li>wheelchairs</li>
    </ul>

    <aside class="brand-band">
      <div class="brand">
        <div class="brand-name"><span class="brand-dot"></span>Stride DME</div>
        <div class="brand-tagline">Durable Medical Equipment</div>
      </div>
    </aside>
  </article>
</body>
</html>
```